This book will apply the 12 Steps to gaming addiction, also known as video game addiction. The primary purpose of the book is to provide an effective solution for this new type of addiction. The solution is based on the rich and successful concepts of traditional twelve-step programs like RL.

The title on the cover will be "Nine Doors Past the Glowing Screen" and "by Martin Quorby". A subtitle can be used if it works in your design of "A Practical Path Beyond Compulsive Console Play". Cover will be for a 6" x 9" book approximately 110 pages in length.

Some back cover text including some review quotes and an author bio are in the attached Word doc. There is also an author photo attached for for the back cover.

Requirements
Must have
• For the cover design it could be stylized, or an image, a partial image, or whatever. I am open to suggestions. Think about what would be noticed by a person searching for help with moderating their video game use, or by the parents or loved ones of problem gamers. Something contemporary and eye catching.

```html
<!DOCTYPE html>
<html lang="en">
<head>
<meta charset="utf-8">
<title>Nine Doors Past the Glowing Screen — Cover Wrap</title>
<link rel="stylesheet" href="https://fonts.googleapis.com/css2?family=Cinzel:wght@400;500&family=Crimson+Text:wght@400;600&family=Libre+Baskerville&family=Silkscreen:wght@700&display=swap">
<style>
  :root {
    --backdrop: #f2f2f2;
    --paper: #ffffff;
    --ink: #111111;
    --title-red: #b3141c;
    --band-grey: #2a2a2a;
    --rule: #d9d9d9;
  }
  * { box-sizing: border-box; margin: 0; padding: 0; }
  html, body { width: 899px; height: 1200px; overflow: hidden; }
  body { background: var(--backdrop); position: relative; font-family: "Crimson Text", Georgia, serif; color: var(--ink); }

  .cover-wrap {
    position: absolute; left: 20px; top: 295px; width: 859px; height: 610px;
    background: var(--paper); display: flex; box-shadow: 0 2px 10px rgba(0,0,0,.18);
  }

  /* Back panel */
  .back-panel { width: 405px; height: 100%; padding: 40px 30px 0 36px; position: relative; font-size: 7.6px; line-height: 1.32; }
  .praise-heading { text-align: center; font-size: 8px; letter-spacing: .2px; margin-bottom: 9px; }
  .praise-quote { margin-bottom: 8px; text-align: justify; }
  .section-break { margin: 6px 0 10px; }
  .blurb p { text-align: justify; margin-bottom: 9px; }
  .author-block { position: absolute; left: 36px; right: 30px; top: 430px; display: flex; gap: 8px; }
  .author-photo { width: 124px; height: 118px; flex: none; background: linear-gradient(160deg, #6d7a55 0%, #a88d6c 45%, #1f2a3c 100%); }
  .author-bio { font-size: 9px; line-height: 1.28; text-align: justify; }

  /* Spine */
  .spine { width: 52px; height: 100%; position: relative; border-left: 1px solid var(--rule); border-right: 1px solid var(--rule); }
  .spine-title, .spine-author {
    position: absolute; left: 50%; white-space: nowrap; transform-origin: center;
    transform: translate(-50%, -50%) rotate(90deg);
  }
  .spine-title { top: 200px; font-family: "Cinzel", serif; font-size: 13px; }
  .spine-title .accent { color: var(--title-red); font-family: "Libre Baskerville", serif; }
  .spine-title .pixel { font-family: "Silkscreen", monospace; font-weight: 700; font-size: 12px; }
  .spine-author { top: 540px; font-family: "Cinzel", serif; font-size: 12px; }

  /* Front panel */
  .front-panel { flex: 1; height: 100%; position: relative; text-align: center; }
  .chain-band { position: absolute; top: 52px; height: 7px; background: var(--band-grey); border-radius: 4px; }
  .chain-band.left { left: 0; width: 132px; }
  .chain-band.right { right: 0; width: 132px; }
  .title-small { position: absolute; top: 36px; left: 0; right: 0; font-family: "Cinzel", serif; font-size: 28px; }
  .title-red { position: absolute; top: 68px; left: 0; right: 0; font-family: "Libre Baskerville", serif; font-size: 64px; color: var(--title-red); letter-spacing: 1px; }
  .title-mid { position: absolute; top: 152px; left: 0; right: 0; font-family: "Cinzel", serif; font-size: 32px; letter-spacing: 1px; }
  .title-pixel { position: absolute; left: 0; right: 0; font-family: "Silkscreen", monospace; font-weight: 700; white-space: nowrap; }
  .title-pixel.one { top: 196px; font-size: 50px; }
  .title-pixel.two { top: 258px; font-size: 50px; }
  .cover-art {
    position: absolute; left: 0; right: 0; top: 362px; height: 160px;
    background: radial-gradient(ellipse at 55% 55%, #3a3a3a 0%, #555 28%, #e8e8e8 60%, #ffffff 78%);
  }
  .front-author { position: absolute; left: 0; right: 0; bottom: 36px; font-family: "Cinzel", serif; font-size: 19px; }
</style>
</head>
<body>
  <main class="cover-wrap">
    <section class="back-panel">
      <h2 class="praise-heading">PRAISE FOR NINE DOORS PAST THE GLOWING SCREEN</h2>
      <p class="praise-quote">“A must-read for anyone who is addicted to or thinks they may have a problem with digital gaming. This eloquent work will also be useful to academics and clinicians exploring potential solutions. The author recognizes the similarities between gaming addiction and other addictions, and logically applies one of the most effective known solutions for addiction - The Twelve Steps.”<br>-- Dale Penrose, Noted Interventionist and Keynote Speaker</p>
      <p class="praise-quote">“If you suffer from digital gaming addiction, I strongly encourage you to use this book as your road map to get you back to the real world.”<br>-- Owen Hartlowe, Founder of Signal Street Review.<br>“As a high school teacher for 24 years, husband, father, coach, and 12-Step member, I can assure you that this book will transform the life of anyone who is addicted to video games. Well written, easy to understand, and a wonderful book that will provide you with a clear road map to recovery, and this includes teenagers, a group I have been working with in the classroom for decades.”<br>-- Leo Varga, Harbor Vale, OR High School Teacher.</p>
      <p class="section-break">******** OR SOME OTHER BREAK TO SEPARATE SECTIONS</p>
      <div class="blurb">
        <p>A Practical Path Beyond Compulsive Console Play (aka Video Game Addiction) based on the rich and successful tradition of the Twelve Steps.</p>
        <p>Addiction to Digital Gaming is a new and troubling phenomenon that has burst upon an unprepared society with alarming speed. Many people crave the use of Digital Games in a strikingly similar way to any other addict. Digital Games are a complex software and hardware system that have been designed to promote continued and progressive usage. This sophisticated technology clearly feeds on natural addictive tendencies.</p>
        <p>The 12 Steps are one of the most effective methods for treating addiction in human history. Originating with Recovery League in 1939, the 12 Steps have since been used to treat a variety of other addictions, including drugs, sex, gambling, eating disorders, and many others. Now in this groundbreaking work the 12 Steps are applied to the complex and evolving contemporary phenomenon of Digital Gaming Addiction.</p>
      </div>
      <div class="author-block">
        <div class="author-photo" role="img" aria-label="Author portrait photograph"></div>
        <p class="author-bio">Martin Quorby is a Technology Consultant and Writer with many years of professional coding and consulting experience. He also struggled with addiction to drugs and alcohol and is now clean and sober in a Twelve-Step program for over 17 years. This unique combination of 12-Step experience and technology expertise led him to create Nine Doors Past the Glowing Screen.</p>
      </div>
    </section>

    <section class="spine">
      <p class="spine-title">NINE <span class="accent">DOORS</span> PAST THE <span class="pixel">GLOWING SCREEN</span></p>
      <p class="spine-author">BY MARTIN QUORBY</p>
    </section>

    <section class="front-panel">
      <span class="chain-band left"></span>
      <span class="chain-band right"></span>
      <h1>
        <span class="title-small">NINE</span>
        <span class="title-red">DOORS</span>
        <span class="title-mid">PAST THE</span>
        <span class="title-pixel one">GLOWING</span>
        <span class="title-pixel two">SCREEN</span>
      </h1>
      <div class="cover-art" role="img" aria-label="Black game controller bound by crossed chains"></div>
      <p class="front-author">BY MARTIN QUORBY</p>
    </section>
  </main>
</body>
</html>
```